MOLVT Study flyer

I need help designing a flyer for a research study that will include brain imaging in adolescents. The info is in the attached document. The study is called the Marrowby Orchard Lantern Vesper Trail (MOLVT) study. Ideally this would be returned as a document that I can edit in the future as we will have several new recruitment phases (different age groups, etc. I also would love to have a logo designed as part of this project, but I recognize that might be a separate design request.

```html
<!DOCTYPE html>
<html lang="en">
<head>
<meta charset="utf-8">
<title>MOLVT Study Flyer</title>
<link rel="stylesheet" href="https://fonts.googleapis.com/css2?family=Jost:wght@300;400;500&family=Source+Serif+4:opsz,wght@8..60,400&display=swap">
<style>
  :root {
    --paper: #ecebe9;
    --footer: #e7e5e3;
    --ink: #1b1b1b;
    --purple: #9a82bd;
    --lavender: #cdbfdc;
    --lavender-soft: #ddd3e8;
    --night: #161616;
    --rule: #c9c4cc;
  }
  * { margin: 0; padding: 0; box-sizing: border-box; }
  html, body { width: 800px; height: 1200px; overflow: hidden; background: var(--paper); }
  body { font-family: "Jost", sans-serif; color: var(--ink); }
  .flyer { position: relative; width: 800px; height: 1200px; overflow: hidden; background: var(--paper); }
  .abs { position: absolute; }

  .hero-photo {
    left: 290px; top: 0; width: 510px; height: 1000px;
    background:
      radial-gradient(ellipse at 62% 22%, #d9d6d4 0%, #bdb9b7 30%, transparent 60%),
      radial-gradient(ellipse at 80% 70%, #8f8893 0%, #b8b0bd 40%, transparent 75%),
      linear-gradient(90deg, var(--paper) 0%, #d8d5d4 30%, #b9b4b8 100%);
  }

  .study-mark { left: 30px; top: 34px; font-size: 52px; font-weight: 400; letter-spacing: 0.26em; color: var(--purple); line-height: 1; }
  .study-name { left: 31px; top: 108px; font-size: 10.5px; letter-spacing: 0.12em; line-height: 20px; text-transform: uppercase; }

  .tagline { left: 650px; top: 47px; font-size: 11px; letter-spacing: 0.16em; line-height: 22px; color: var(--purple); text-transform: uppercase; }
  .tagline-rule { left: 650px; top: 144px; width: 27px; height: 2px; background: var(--purple); }

  .headline { left: 30px; top: 215px; font-family: "Source Serif 4", serif; font-size: 44px; line-height: 46px; letter-spacing: -0.01em; }
  .headline .accent { color: var(--purple); }
  .headline-rule { left: 31px; top: 419px; width: 29px; height: 1px; background: var(--purple); }

  .intro { left: 31px; top: 439px; width: 260px; font-size: 12px; line-height: 20.5px; }

  .question { left: 31px; top: 573px; padding-left: 16px; border-left: 1px solid var(--ink); font-size: 13px; letter-spacing: 0.12em; line-height: 20px; text-transform: uppercase; }
  .question .ask { margin-bottom: 5px; }
  .question .prompt { color: var(--purple); }

  .eligibility-panel { left: 310px; top: 684px; width: 490px; height: 312px; background: var(--lavender); opacity: 0.92; }

  .section-label { font-size: 11px; letter-spacing: 0.16em; text-transform: uppercase; }
  .participation-label { left: 38px; top: 711px; color: var(--purple); }

  .step { left: 38px; width: 244px; display: flex; gap: 16px; }
  .step-icon { flex: none; width: 64px; height: 64px; border-radius: 50%; background: var(--lavender-soft); display: flex; align-items: center; justify-content: center; }
  .step-text { font-size: 11px; line-height: 16.5px; padding-top: 4px; }
  .step-text b { display: block; font-weight: 400; letter-spacing: 0.1em; text-transform: uppercase; }
  .step-rule { left: 118px; width: 164px; height: 1px; background: var(--rule); }

  .eligibility-label { left: 337px; top: 720px; line-height: 18px; font-size: 10.5px; }
  .eligibility-rule { left: 337px; top: 765px; width: 26px; height: 1px; background: var(--ink); }
  .criterion { left: 337px; display: flex; gap: 16px; font-size: 11.5px; line-height: 18px; }
  .criterion svg { flex: none; margin-top: -2px; }

  .contact-band { left: 310px; top: 996px; width: 490px; height: 106px; background: var(--night); color: #f2f0f2; }
  .contact-icon { left: 24px; top: 22px; width: 55px; height: 55px; border: 1px solid #8d8d8d; border-radius: 50%; display: flex; align-items: center; justify-content: center; }
  .contact-call { left: 94px; top: 25px; font-size: 9.5px; letter-spacing: 0.1em; line-height: 18px; text-transform: uppercase; }
  .contact-call .lead { color: var(--purple); }
  .contact-call .note { text-transform: none; letter-spacing: 0.02em; margin-top: 6px; font-size: 9.5px; }
  .contact-divider { left: 271px; top: 20px; width: 1px; height: 56px; background: #6a6a6a; }
  .contact-email { left: 294px; top: 28px; font-size: 14px; letter-spacing: 0.01em; }
  .contact-pay { left: 294px; top: 60px; font-size: 9.5px; letter-spacing: 0.1em; color: var(--purple); text-transform: uppercase; }

  .footer { left: 0; top: 1102px; width: 800px; height: 98px; background: var(--footer); }
  .institution { left: 38px; top: 30px; font-family: "Source Serif 4", serif; font-size: 22px; line-height: 26px; width: 200px; }
  .footer-divider { top: 24px; width: 1px; height: 54px; background: var(--rule); }
  .footer-note { font-size: 9.5px; line-height: 15.5px; }
  .lock-icon { left: 563px; top: 25px; width: 50px; height: 50px; border-radius: 50%; background: var(--lavender); display: flex; align-items: center; justify-content: center; }
</style>
</head>
<body>
<main class="flyer">
  <div class="abs hero-photo" role="img" aria-label="Black and white portrait of a teenage girl gazing upward, blended with a lavender-tinted brain scan image and fine wave lines"></div>

  <div class="abs study-mark">MOLVT</div>
  <div class="abs study-name">Marrowby Orchard Lantern<br>Vesper Trail Study</div>

  <div class="abs tagline">Exploring<br>the developing<br>adolescent<br>mind</div>
  <div class="abs tagline-rule"></div>

  <h1 class="abs headline" style="font-weight:400">Understanding<br>today.<br><span class="accent">Transforming<br>tomorrow.</span></h1>
  <div class="abs headline-rule"></div>

  <p class="abs intro">Calder Ridge University researchers are studying how emotions, decision-making, and puberty influence adolescent brain development.</p>

  <div class="abs question">
    <p class="ask">Are you the parent of a<br>child age 10–17?</p>
    <p class="prompt">Do they worry or overthink<br>negative emotions?</p>
  </div>

  <div class="abs eligibility-panel"></div>

  <h2 class="abs section-label participation-label" style="font-weight:400">Study participation involves:</h2>

  <div class="abs step" style="top:744px">
    <div class="step-icon">
      <svg width="32" height="30" viewBox="0 0 32 30" fill="none" stroke="#222" stroke-width="1.4"><path d="M3 3h26v17H13l-7 6v-6H3z" stroke-linejoin="round"/><circle cx="11" cy="11.5" r="1" fill="#222"/><circle cx="16" cy="11.5" r="1" fill="#222"/><circle cx="21" cy="11.5" r="1" fill="#222"/></svg>
    </div>
    <p class="step-text"><b>One one-hour interview</b>(online or in-person) where your child will discuss their thoughts</p>
  </div>
  <div class="abs step-rule" style="top:826px"></div>

  <div class="abs step" style="top:829px">
    <div class="step-icon">
      <svg width="26" height="32" viewBox="0 0 26 32" fill="none" stroke="#222" stroke-width="1.4"><rect x="2" y="4" width="22" height="27" rx="2"/><rect x="8" y="1.5" width="10" height="5" rx="1"/><path d="M6 13l1.5 1.5L10 12M6 19l1.5 1.5L10 18M6 25l1.5 1.5L10 24M13 13h7M13 19h7M13 25h7"/></svg>
    </div>
    <p class="step-text" style="padding-top:20px"><b>Online questionnaires</b>(parent and child)</p>
  </div>
  <div class="abs step-rule" style="top:898px"></div>

  <div class="abs step" style="top:914px">
    <div class="step-icon">
      <svg width="36" height="30" viewBox="0 0 36 30" fill="none" stroke="#222" stroke-width="1.3"><path d="M18 3c-3-2-8-1-9 3-4 0-6 4-4 7-3 2-2 7 2 8 0 4 5 6 8 4 1 1 2 2 3 2V3zM18 3c3-2 8-1 9 3 4 0 6 4 4 7 3 2 2 7-2 8 0 4-5 6-8 4-1 1-2 2-3 2"/><path d="M10 11c2 0 3 1 3 3M26 11c-2 0-3 1-3 3M11 19c2-1 4 0 4 2M25 19c-2-1-4 0-4 2"/></svg>
    </div>
    <p class="step-text"><b>One two-hour visit</b>where your child will complete an MRI scan, answer questions about their puberty stage, and have a small hair sample taken to study puberty hormones</p>
  </div>

  <h2 class="abs section-label eligibility-label" style="font-weight:400">Your child may be<br>eligible if they:</h2>
  <div class="abs eligibility-rule"></div>

  <div class="abs criterion" style="top:787px">
    <svg width="21" height="21" viewBox="0 0 21 21" fill="none" stroke="#222" stroke-width="1.2"><circle cx="10.5" cy="10.5" r="9.5"/><path d="M6 10.5l3 3 6-6"/></svg>
    <span>Are age 10–17</span>
  </div>
  <div class="abs criterion" style="top:821px">
    <svg width="21" height="21" viewBox="0 0 21 21" fill="none" stroke="#222" stroke-width="1.2"><circle cx="10.5" cy="10.5" r="9.5"/><path d="M6 10.5l3 3 6-6"/></svg>
    <span>Tend to worry or<br>overthink negative<br>thoughts</span>
  </div>
  <div class="abs criterion" style="top:891px">
    <svg width="21" height="21" viewBox="0 0 21 21" fill="none" stroke="#222" stroke-width="1.2"><circle cx="10.5" cy="10.5" r="9.5"/><path d="M6 10.5l3 3 6-6"/></svg>
    <span>Have not been<br>diagnosed with<br>psychosis, learning<br>problems, or autism</span>
  </div>

  <section class="abs contact-band">
    <div class="abs contact-icon">
      <svg width="28" height="20" viewBox="0 0 28 20" fill="none" stroke="#f2f0f2" stroke-width="1.3"><rect x="1" y="1" width="26" height="18"/><path d="M1 1l13 10L27 1M1 19l10-9M27 19l-10-9"/></svg>
    </div>
    <div class="abs contact-call">
      <p class="lead">Interested in participating?</p>
      <p>Want more information?</p>
      <p class="note">Please contact us!</p>
    </div>
    <div class="abs contact-divider"></div>
    <p class="abs contact-email">molvtstudy@calderridge.edu</p>
    <p class="abs contact-pay">Compensation up to $140</p>
  </section>

  <footer class="abs footer">
    <p class="abs institution">Calder Ridge<br>University</p>
    <div class="abs footer-divider" style="left:281px"></div>
    <p class="abs footer-note" style="left:317px;top:22px">This study is conducted by<br>researchers at Calder Ridge<br>University.<br>All information is kept confidential.</p>
    <div class="abs footer-divider" style="left:533px"></div>
    <div class="abs lock-icon">
      <svg width="18" height="22" viewBox="0 0 18 22" fill="none" stroke="#222" stroke-width="1.4"><rect x="1.5" y="9" width="15" height="12" rx="1.5"/><path d="M4.5 9V6a4.5 4.5 0 019 0v3"/><circle cx="9" cy="14" r="1.3" fill="#222"/><path d="M9 15v2.5"/></svg>
    </div>
    <p class="abs footer-note" style="left:630px;top:34px">Your child’s safety and<br>comfort are our<br>top priority.</p>
  </footer>
</main>
</body>
</html>
```